Kestrel Golf Circle Chart

I would like some type of design that can then be used on our website, like a png. or .jpeg or vector format. We want a circle/flow chart that describes our golf coaching process and has our logo faded in the background. attached is a rough draft to give you a general idea..something I created in word document but would like a much better version and attached is our logo. Our colors are red, black, and grey. The design does not necessarily have to have all of the bullet points..

Target Market(s)

Golfers, junior high golfers, high school golfers, adult golfers

Font styles to use
Sans Serif

Colors
ec1f27
f04a50
f59296
fbd4d5
aaaaaa
cbcbcb
1b1b1b
474747

Requirements
Nice to have
• Our colors are red, black, and grey, do not have to use all 3 in one design. Also The design does not necessarily have to have all of the bullet points.

```html
<!DOCTYPE html>
<html lang="en">
<head>
<meta charset="utf-8">
<title>Kestrel Golf Coaching Process</title>
<link rel="stylesheet" href="https://fonts.googleapis.com/css2?family=Bebas+Neue&family=Merriweather:wght@400&display=swap">
<style>
  :root {
    --red: #ec1f27;
    --black: #1b1b1b;
    --grey-dark: #474747;
    --white: #ffffff;
    --bg: #fafafa;
  }
  html, body {
    margin: 0;
    padding: 0;
    width: 1200px;
    height: 1200px;
    overflow: hidden;
    background: var(--bg);
  }
  .process-chart { display: block; width: 1200px; height: 1200px; }
  .step-arrow { fill: var(--black); filter: drop-shadow(0 6px 8px rgba(0,0,0,.35)); }
  .step-title {
    font-family: "Bebas Neue", "Arial Narrow", sans-serif;
    fill: var(--red);
    font-size: 84px;
  }
  .step-item {
    font-family: "Merriweather", Georgia, serif;
    fill: var(--white);
    font-size: 21px;
  }
  .step-rule { stroke: var(--grey-dark); stroke-width: 1.5; }
  .ring { fill: var(--red); }
  .orbit { fill: none; stroke: var(--red); stroke-width: 3; stroke-dasharray: 2 6; }
  .brand-name {
    font-family: "Bebas Neue", "Arial Narrow", sans-serif;
    fill: var(--red);
    font-size: 110px;
  }
</style>
</head>
<body>
<svg class="process-chart" viewBox="0 0 1500 1500" xmlns="http://www.w3.org/2000/svg">
  <defs>
    <radialGradient id="ball-shade" cx="40%" cy="35%" r="70%">
      <stop offset="0" stop-color="#ffffff"/>
      <stop offset="0.6" stop-color="#e9e9eb"/>
      <stop offset="1" stop-color="#c4c6ca"/>
    </radialGradient>
  </defs>

  <circle class="orbit" cx="735" cy="740" r="400"/>
  <circle class="ring" cx="735" cy="740" r="380"/>

  <!-- Evaluation -->
  <polygon class="step-arrow" points="365,548 455,262 622,205 615,162 800,225 706,408 692,387 375,555"/>
  <g transform="translate(462 330) rotate(-24)">
    <text class="step-title" x="0" y="0" textLength="238" lengthAdjust="spacingAndGlyphs">EVALUATION</text>
    <text class="step-item" x="16" y="45" textLength="212" lengthAdjust="spacingAndGlyphs">Video Swing Analysis</text>
    <line class="step-rule" x1="14" y1="59" x2="236" y2="59"/>
    <text class="step-item" x="44" y="80" textLength="162" lengthAdjust="spacingAndGlyphs">Putting Reports</text>
    <line class="step-rule" x1="30" y1="94" x2="236" y2="94"/>
    <text class="step-item" x="43" y="115" textLength="165" lengthAdjust="spacingAndGlyphs">Develope a Plan</text>
  </g>

  <!-- Coaching -->
  <polygon class="step-arrow" points="940,367 1215,455 1248,625 1312,625 1245,805 1065,712 1082,698 875,383"/>
  <text class="step-title" transform="rotate(14.5 992 465)" x="992" y="465" textLength="205" lengthAdjust="spacingAndGlyphs">COACHING</text>
  <text class="step-item" transform="rotate(-18 1143 572)" x="1143" y="572" text-anchor="middle" textLength="128" lengthAdjust="spacingAndGlyphs">Tour Quality</text>
  <text class="step-item" transform="rotate(-18 1150 596)" x="1150" y="596" text-anchor="middle" textLength="118" lengthAdjust="spacingAndGlyphs">Technology</text>
  <line class="step-rule" transform="rotate(-18 1162 608)" x1="1080" y1="608" x2="1244" y2="608"/>
  <text class="step-item" transform="rotate(-18 1163 630)" x="1163" y="630" text-anchor="middle" textLength="150" lengthAdjust="spacingAndGlyphs">Visualization &amp;</text>
  <text class="step-item" transform="rotate(-18 1178 653)" x="1178" y="653" text-anchor="middle" textLength="98" lengthAdjust="spacingAndGlyphs">Feedback</text>
  <line class="step-rule" transform="rotate(-18 1188 666)" x1="1105" y1="666" x2="1271" y2="666"/>
  <text class="step-item" transform="rotate(-18 1188 685)" x="1188" y="685" text-anchor="middle" textLength="120" lengthAdjust="spacingAndGlyphs">Understand</text>
  <text class="step-item" transform="rotate(-18 1198 708)" x="1198" y="708" text-anchor="middle" textLength="158" lengthAdjust="spacingAndGlyphs">Inconsistencies</text>

  <!-- Practice -->
  <polygon class="step-arrow" points="1095,885 1105,942 1022,1215 850,1282 852,1318 668,1250 770,1072 778,1090"/>
  <g transform="translate(782 1165) rotate(-23)">
    <text class="step-title" x="0" y="0" textLength="200" lengthAdjust="spacingAndGlyphs">PRACTICE</text>
  </g>
  <g transform="translate(790 1222) rotate(-25.5)">
    <text class="step-item" x="0" y="0" textLength="228" lengthAdjust="spacingAndGlyphs">24/7 Access to Practice</text>
    <line class="step-rule" x1="0" y1="14" x2="240" y2="14"/>
    <text class="step-item" x="-2" y="36" textLength="236" lengthAdjust="spacingAndGlyphs">Practice with a Purpose</text>
  </g>

  <!-- Track Data -->
  <polygon class="step-arrow" points="155,858 215,675 405,770 385,785 522,1092 548,1112 262,1022 180,860"/>
  <text class="step-item" transform="rotate(-22.5 292 849)" x="292" y="849" text-anchor="middle" textLength="152" lengthAdjust="spacingAndGlyphs">Track Progress</text>
  <text class="step-item" transform="rotate(-22.5 300 876)" x="300" y="876" text-anchor="middle" textLength="98" lengthAdjust="spacingAndGlyphs">with Data</text>
  <text class="step-title" transform="rotate(17.5 270 1010)" x="270" y="1010" textLength="210" lengthAdjust="spacingAndGlyphs">TRACK DATA</text>

  <!-- Centre ball with brand name -->
  <circle cx="735" cy="740" r="282" fill="url(#ball-shade)" role="img" aria-label="Dimpled white golf ball"/>
  <text class="brand-name" x="735" y="778" text-anchor="middle">Kestrel Golf</text>
</svg>
</body>
</html>
```